Harbor Ridge Casting business card
Derek Halloway
Project: Harbor Ridge Casting business card
Harbor Ridge Casting business card - Manufacturing
Creative Brief
Simple
4307 Tilden Street Irvine, CA 92618
949-617-4380 x35
derek@harborridgecasting.com
www.harborridgecasting.com

```html
<!DOCTYPE html>
<html lang="en">
<head>
<meta charset="utf-8">
<title>Harbor Ridge Casting Stationery</title>
<link href="https://fonts.googleapis.com/css2?family=Open+Sans:wght@400;600;700&display=swap" rel="stylesheet">
<style>
  :root {
    --navy: #2e4577;
    --orange: #e4582a;
    --paper: #ffffff;
    --backdrop: #f3f3f3;
    --ink: #6b6f78;
    --edge: #e2e2e2;
  }
  * { margin: 0; padding: 0; box-sizing: border-box; }
  html, body { width: 1200px; height: 937px; overflow: hidden; }
  body {
    background: var(--backdrop);
    font-family: "Open Sans", Arial, sans-serif;
    position: relative;
  }
  .sheet {
    position: absolute;
    background: var(--paper);
    border: 1px solid var(--edge);
    box-shadow: 0 2px 6px rgba(0,0,0,0.08);
    overflow: hidden;
  }

  /* Footer band: flat slanted navy block with a thin orange bar */
  .band { position: absolute; left: 0; bottom: 0; width: 100%; }
  .band .band-fill { fill: var(--navy); }
  .band .band-accent { fill: var(--orange); }

  /* Brand line: square marker beside the name */
  .brand { display: flex; align-items: center; }
  .brand-mark { background: var(--orange); flex: none; }
  .brand-text { display: flex; flex-direction: column; }
  .brand-name { color: var(--navy); font-weight: 700; white-space: nowrap; line-height: 1.1; }
  .brand-tagline { color: var(--navy); font-weight: 600; letter-spacing: 0.04em; white-space: nowrap; }

  /* Letterhead */
  .letterhead { left: 182px; top: 56px; width: 390px; height: 551px; }
  .letterhead .brand { position: absolute; left: 30px; top: 40px; gap: 7px; }
  .letterhead .brand-mark { width: 16px; height: 16px; }
  .letterhead .brand-name { font-size: 13px; }
  .letterhead .brand-tagline { font-size: 5px; }
  .letter-body { position: absolute; left: 30px; top: 140px; width: 320px; font-size: 6px; line-height: 1.55; color: var(--ink); }
  .letter-body p { margin-bottom: 9px; }
  .signature { width: 40px; height: 14px; background: linear-gradient(90deg, #c9ccd3, #e6e7ea); margin: 4px 0 6px; }
  .letter-contact { position: absolute; right: 22px; bottom: 22px; color: #fff; font-size: 5.5px; line-height: 1.6; text-align: right; }

  /* Folder */
  .folder { left: 633px; top: 35px; width: 536px; height: 587px; }
  .folder .brand { position: absolute; left: 0; right: 0; top: 292px; justify-content: center; gap: 16px; }
  .folder .brand-mark { width: 44px; height: 44px; }
  .folder .brand-name { font-size: 34px; }
  .folder .brand-tagline { font-size: 13px; margin-top: 2px; }
  .folder-url { position: absolute; right: 34px; bottom: 18px; color: #fff; font-size: 11px; letter-spacing: 0.18em; font-weight: 600; }

  /* Business cards */
  .card { width: 177px; height: 92px; left: 46px; }
  .card-front { top: 663px; }
  .card-back { top: 769px; }
  .card-front .brand { position: absolute; left: 8px; top: 18px; gap: 3px; }
  .card-front .brand-mark { width: 7px; height: 7px; }
  .card-front .brand-name { font-size: 6px; }
  .card-front .brand-tagline { font-size: 2.8px; }
  .card-details { position: absolute; left: 98px; top: 12px; font-size: 3.6px; line-height: 1.55; color: var(--ink); }
  .card-details .person { color: var(--navy); font-weight: 700; font-size: 4.4px; }
  .card-back .brand { position: absolute; left: 0; right: 0; top: 28px; justify-content: center; gap: 5px; }
  .card-back .brand-mark { width: 10px; height: 10px; }
  .card-back .brand-name { font-size: 8.5px; }
  .card-back .brand-tagline { font-size: 3.6px; }

  /* Envelope front */
  .envelope-front { left: 263px; top: 663px; width: 445px; height: 198px; }
  .envelope-front .brand { position: absolute; left: 14px; top: 22px; gap: 6px; }
  .envelope-front .brand-mark { width: 13px; height: 13px; }
  .envelope-front .brand-name { font-size: 11px; }
  .envelope-front .brand-tagline { font-size: 4.5px; }
  .envelope-front .band { bottom: 52px; }
  .envelope-url { position: absolute; left: 0; right: 0; bottom: 18px; text-align: center; color: var(--navy); font-size: 10px; letter-spacing: 0.3em; font-weight: 600; }

  /* Envelope back */
  .envelope-back { left: 739px; top: 663px; width: 425px; height: 198px; }
  .envelope-back .flap { position: absolute; left: 0; top: 0; width: 100%; height: 100%; }
  .envelope-back .flap-fill { fill: var(--navy); }
  .envelope-back .fold { fill: none; stroke: var(--edge); stroke-width: 1; }
  .flap-url { position: absolute; right: 26px; top: 42px; color: #fff; font-size: 9px; letter-spacing: 0.16em; font-weight: 600; }
</style>
</head>
<body>

<section class="sheet letterhead">
  <div class="brand">
    <span class="brand-mark"></span>
    <span class="brand-text">
      <span class="brand-name">Harbor Ridge Casting</span>
      <span class="brand-tagline">PRECISION CASTING PARTNERS</span>
    </span>
  </div>
  <div class="letter-body">
    <p>July 3, 2024<br>Purchasing Office<br>Dear Partner,</p>
    <p>Thank you for choosing our foundry for your next tooling program. Our team has reviewed the drawings and prepared a schedule that keeps every milestone on track.</p>
    <p>Each mold is machined, polished and tested in house before shipment, so quality stays consistent from the first shot to the last.</p>
    <p>Please contact me with any questions about pricing or lead times.</p>
    <p>Sincerely,</p>
    <div class="signature" role="img" aria-label="Handwritten signature"></div>
    <p>Derek Halloway<br>Sales Manager</p>
  </div>
  <svg class="band" viewBox="0 0 390 100" preserveAspectRatio="none" height="100">
    <polygon class="band-accent" points="0,30 390,8 390,12 0,34"/>
    <polygon class="band-fill" points="0,42 390,20 390,100 0,100"/>
  </svg>
  <div class="letter-contact">
    4307 Tilden Street Irvine, CA 92618<br>
    949-617-4380 x35<br>
    derek@harborridgecasting.com<br>
    www.harborridgecasting.com
  </div>
</section>

<section class="sheet folder">
  <div class="brand">
    <span class="brand-mark"></span>
    <span class="brand-text">
      <span class="brand-name">Harbor Ridge Casting</span>
      <span class="brand-tagline">PRECISION CASTING PARTNERS</span>
    </span>
  </div>
  <svg class="band" viewBox="0 0 536 150" preserveAspectRatio="none" height="150">
    <polygon class="band-accent" points="0,36 536,6 536,11 0,41"/>
    <polygon class="band-fill" points="0,52 536,22 536,150 0,150"/>
  </svg>
  <div class="folder-url">www.harborridgecasting.com</div>
</section>

<section class="sheet card card-front">
  <div class="brand">
    <span class="brand-mark"></span>
    <span class="brand-text">
      <span class="brand-name">Harbor Ridge Casting</span>
      <span class="brand-tagline">PRECISION CASTING PARTNERS</span>
    </span>
  </div>
  <div class="card-details">
    <div class="person">Derek Halloway</div>
    <div>Sales Manager</div>
    <div>949-617-4380 x35</div>
    <div>derek@harborridgecasting.com</div>
    <div>4307 Tilden Street Irvine, CA 92618</div>
  </div>
  <svg class="band" viewBox="0 0 177 30" preserveAspectRatio="none" height="30">
    <polygon class="band-accent" points="0,10 177,3 177,5 0,12"/>
    <polygon class="band-fill" points="0,15 177,8 177,30 0,30"/>
  </svg>
</section>

<section class="sheet card card-back">
  <div class="brand">
    <span class="brand-mark"></span>
    <span class="brand-text">
      <span class="brand-name">Harbor Ridge Casting</span>
      <span class="brand-tagline">PRECISION CASTING PARTNERS</span>
    </span>
  </div>
  <svg class="band" viewBox="0 0 177 26" preserveAspectRatio="none" height="26">
    <polygon class="band-accent" points="0,9 177,3 177,5 0,11"/>
    <polygon class="band-fill" points="0,14 177,8 177,26 0,26"/>
  </svg>
</section>

<section class="sheet envelope-front">
  <div class="brand">
    <span class="brand-mark"></span>
    <span class="brand-text">
      <span class="brand-name">Harbor Ridge Casting</span>
      <span class="brand-tagline">PRECISION CASTING PARTNERS</span>
    </span>
  </div>
  <svg class="band" viewBox="0 0 445 60" preserveAspectRatio="none" height="60">
    <polygon class="band-accent" points="0,30 445,6 445,10 0,34"/>
    <polygon class="band-fill" points="0,42 445,18 445,36 0,60"/>
  </svg>
  <div class="envelope-url">www.harborridgecasting.com</div>
</section>

<section class="sheet envelope-back">
  <svg class="flap" viewBox="0 0 425 198" preserveAspectRatio="none">
    <path class="flap-fill" d="M0 0 H425 V78 C300 104 130 100 0 84 Z"/>
    <path class="fold" d="M0 198 L212 120 L425 198"/>
  </svg>
  <div class="flap-url">www.harborridgecasting.com</div>
</section>

</body>
</html>
```